Brell Harbor Company Business Cards

Front and Back Business Card - logo and text setup - cool design. I need workable photoshop or illustrator files so I can setup each employee card with design that is created
Updates

Hi everyone, thank you for the great entries. Please no more white and blue cards - there are so many already - black and silver only now please. thanks!

Target Market(s)

Construction Industry - Facility Managers

Industry/Entity Type

Construction

Contact Information for Business Card

I really like contemporary simplistic looks - clean neat....not opposed to seeing some black backrounds

Requirements
Must have
• Logo/website address with design on front only - www.brellharbor-example.com (logo attached)
• Back:
• Name/Title/Company Address/Phone/email address
Nice to have
• Cool design
Should not have
• Nothing gimmicky like Fire or Water - since we are a Fire Protection company - it has all been done

```html
<!DOCTYPE html>
<html lang="en">
<head>
<meta charset="utf-8">
<title>Brell Harbor Company Business Cards</title>
<link rel="stylesheet" href="https://fonts.googleapis.com/css2?family=Open+Sans:wght@400;600;700;800&display=swap">
<style>
  :root {
    --stage: #2e3034;
    --card: #ffffff;
    --navy: #24427d;
    --red: #e0442a;
    --ink: #2f2f33;
  }
  * { box-sizing: border-box; margin: 0; padding: 0; }
  html, body {
    width: 1200px; height: 1000px; overflow: hidden;
    background: var(--stage);
    font-family: "Open Sans", sans-serif;
  }
  .canvas { position: relative; width: 1200px; height: 1000px; }
  .card {
    position: absolute; left: 250px; width: 700px; height: 400px;
    background: var(--card); overflow: hidden;
    box-shadow: 0 10px 30px rgba(0,0,0,.45);
  }
  .card--back { top: 60px; }
  .card--front { top: 540px; }

  .brand-name {
    font-weight: 800; color: var(--navy); letter-spacing: -0.5px;
    white-space: nowrap;
  }
  .card--back .brand-name {
    position: absolute; left: 0; right: 0; top: 140px;
    text-align: center; font-size: 50px;
  }
  .web-band {
    position: absolute; left: 240px; right: 0; top: 290px; height: 44px;
    background: var(--red);
    display: flex; align-items: center; justify-content: flex-end;
    padding-right: 30px;
  }
  .web-band__url {
    color: #fff; font-size: 15px; letter-spacing: 3px; font-weight: 400;
    white-space: nowrap;
  }

  .card--front .brand-name {
    position: absolute; right: 40px; top: 48px;
    font-size: 34px; text-align: right;
  }
  .contact { position: absolute; left: 44px; top: 108px; color: var(--ink); }
  .contact__name { font-size: 22px; font-weight: 700; color: var(--navy); line-height: 1.1; }
  .contact__title { font-size: 16px; font-weight: 400; color: var(--red); letter-spacing: .5px; margin-bottom: 10px; }
  .contact__address { font-size: 17px; line-height: 1.3; margin-bottom: 4px; }
  .contact__line { display: flex; align-items: center; gap: 10px; font-size: 17px; line-height: 1.35; white-space: nowrap; }
  .contact__icon { width: 16px; height: 16px; fill: var(--navy); flex: none; }

  .tile-row { position: absolute; left: 0; bottom: 0; width: 700px; height: 56px; }
</style>
</head>
<body>
<main class="canvas">

  <section class="card card--back" aria-label="Card back">
    <div class="brand-name">Brell Harbor Company</div>
    <div class="web-band"><span class="web-band__url">www.brellharbor-example.com</span></div>
  </section>

  <section class="card card--front" aria-label="Card front">
    <div class="brand-name">Brell Harbor Company</div>

    <div class="contact">
      <div class="contact__name">MARTEN KALE</div>
      <div class="contact__title">PRESIDENT</div>
      <div class="contact__address">48 Quarry Lane<br>Halvern, NY 11900</div>
      <div class="contact__line">
        <svg class="contact__icon" viewBox="0 0 16 16" aria-hidden="true"><path d="M3 1h3l1.5 4-2 1.3a8 8 0 0 0 4.2 4.2L11 8.5 15 10v3a2 2 0 0 1-2 2A12 12 0 0 1 1 3a2 2 0 0 1 2-2z"/></svg>
        <span>(555) 014-2237</span>
      </div>
      <div class="contact__line">
        <svg class="contact__icon" viewBox="0 0 16 16" aria-hidden="true"><rect x="4" y="1" width="8" height="4"/><rect x="1" y="6" width="14" height="6" rx="1"/><rect x="4" y="10" width="8" height="5" fill="#fff" stroke="#24427d" stroke-width="1.4"/></svg>
        <span>(555) 014-2238</span>
      </div>
      <div class="contact__line">
        <svg class="contact__icon" viewBox="0 0 16 16" aria-hidden="true"><rect x="1" y="3" width="14" height="10" rx="1"/><path d="M1.5 3.8 8 9l6.5-5.2" fill="none" stroke="#fff" stroke-width="1.4"/></svg>
        <span>info@brellharbor-example.com</span>
      </div>
    </div>

    <svg class="tile-row" viewBox="0 0 700 56" aria-hidden="true">
      <rect x="0"   y="14" width="44" height="42" fill="#f8d8cb"/>
      <rect x="64"  y="14" width="44" height="42" fill="#f5cbb9"/>
      <rect x="128" y="14" width="44" height="42" fill="#f2bea8"/>
      <rect x="192" y="14" width="44" height="42" fill="#efb096"/>
      <rect x="256" y="14" width="44" height="42" fill="#eca284"/>
      <rect x="320" y="14" width="44" height="42" fill="#e99373"/>
      <rect x="384" y="14" width="44" height="42" fill="#e68462"/>
      <rect x="448" y="14" width="44" height="42" fill="#e37552"/>
      <rect x="512" y="14" width="44" height="42" fill="#e06642"/>
      <rect x="576" y="14" width="44" height="42" fill="#dd5636"/>
      <rect x="640" y="14" width="60" height="42" fill="#d9432b"/>
    </svg>
  </section>

</main>
</body>
</html>
```